Individual product brochures and one linecard

I am looking for 5 individual product brochures for our main product lines, and one full line card incorporating the 5. The products can be found at our website home page www.brixwellmfg.com (not including the parts and accessories). We cater to the CNC milling and machining industry, particularly in woods and plastics in industrial settings. We can provide many more additional images one placeholders are in place.

```html
<!DOCTYPE html>
<html lang="en">
<head>
<meta charset="utf-8">
<title>Brixwell – CNC Gaskets Brochure</title>
<link href="https://fonts.googleapis.com/css2?family=Poppins:wght@500;600&family=Roboto:wght@400;500;700&display=swap" rel="stylesheet">
<style>
  :root{
    --teal:#1f7f78;
    --teal-line:#3aa59c;
    --ink:#111;
    --body:#1c1c1c;
    --paper:#f3f3f3;
    --page-bg:#ffffff;
    --frame:#2a2a2a;
    --label-bg:#050505;
  }
  *{box-sizing:border-box;margin:0;padding:0}
  html,body{width:800px;height:1200px;overflow:hidden;background:var(--page-bg)}
  .flyer{
    position:absolute;left:10px;top:95px;width:780px;height:1010px;
    background:var(--paper);overflow:hidden;
    box-shadow:0 8px 24px rgba(0,0,0,.35);
    font-family:"Roboto",Arial,sans-serif;color:var(--body);
  }
  .hero{
    position:absolute;left:0;top:0;width:780px;height:207px;
    background:
      radial-gradient(ellipse at 40% 25%,#8a8886 0 5%,transparent 14%),
      linear-gradient(180deg,#9a8470 0%,#b09478 45%,#8e7058 100%);
    border-bottom:3px solid var(--teal-line);
  }
  .brand-name{
    position:absolute;left:26px;top:218px;
    font-family:"Roboto",Arial,sans-serif;font-weight:700;font-size:46px;
    color:var(--teal);letter-spacing:.5px;
  }
  .headline{position:absolute;left:253px;top:251px;line-height:1}
  .headline .lead{
    display:block;font-family:"Poppins",sans-serif;font-weight:600;
    font-size:37px;letter-spacing:2px;color:var(--ink);
  }
  .headline .product{
    display:block;margin-top:6px;font-family:"Roboto",sans-serif;font-weight:700;
    font-size:42px;color:var(--teal);letter-spacing:1px;
  }
  .headline .star{color:var(--ink);font-size:40px;margin-left:6px}
  .product-card{
    position:absolute;width:138px;height:131px;background:#fff;
    border:1px solid var(--frame);padding:6px;
  }
  .product-card .photo{width:100%;height:100%;position:relative}
  .product-card .label{
    position:absolute;left:0;right:0;bottom:0;background:var(--label-bg);
    color:#fff;font-weight:700;font-size:12px;line-height:14px;
    padding:6px 5px 5px;text-transform:uppercase;
  }
  .photo.grid{background:linear-gradient(180deg,#6d6a66 0%,#a79a8a 30%,#8d8377 100%)}
  .photo.tile{background:linear-gradient(180deg,#8e8780 0%,#b9b4ae 50%,#9d968e 100%)}
  .photo.onboard{background:linear-gradient(180deg,#b6b3af 0%,#d2b894 40%,#5a5a5a 100%)}
  .photo.inboard{background:linear-gradient(160deg,#d9cab3 0%,#c8b596 50%,#b9a584 100%)}
  .photo.cover{background:linear-gradient(180deg,#b3ada5 0%,#8f8982 50%,#6f6a64 100%)}
  .copy{position:absolute;font-size:11.5px;line-height:13.8px}
  .copy.right{text-align:right}
  .footer{
    position:absolute;left:0;top:941px;width:780px;height:54px;background:var(--teal);
    color:#fff;font-size:13.5px;
  }
  .footer-base{position:absolute;left:0;top:995px;width:780px;height:15px;background:#000}
  .footer .item{position:absolute;display:flex;align-items:center;gap:8px;line-height:16px}
  .footer .divider{position:absolute;top:8px;width:2px;height:38px;background:#0d3f3b}
  .footer svg{flex:none;fill:#fff}
  .social{position:absolute;left:691px;top:18px;display:flex;gap:8px}
  .social span{width:20px;height:20px;border-radius:50%;background:#fff;opacity:.85}
</style>
</head>
<body>
<div class="flyer">
  <div class="hero" role="img" aria-label="Close-up photo of a CNC router bit cutting wood with sawdust flying"></div>

  <div class="brand-name">Brixwell</div>

  <h1 class="headline">
    <span class="lead">THE ONLY ANSWER FOR</span>
    <span class="product">CNC GASKETS<span class="star">★</span></span>
  </h1>

  <div class="product-card" style="left:24px;top:331px">
    <div class="photo grid" role="img" aria-label="Photo of grid gasketing on a CNC router table">
      <div class="label">Grid Gasketing</div>
    </div>
  </div>
  <p class="copy" style="left:172px;top:370px;width:585px">Grid Gasketing is the non-adhesive material used in the perimeter of the CNC Router table/pod itself. De-pending on the type of router that is being used, both square and rounded products are available. The goal is to fill the channel width-wise and stand proud above the table roughly 1/16 of an inch. This will create an air-tight seal under your spoil board/fixture board</p>

  <div class="product-card" style="left:617px;top:445px">
    <div class="photo tile" role="img" aria-label="Photo of tile gasketing panels on a spoil board">
      <div class="label">Tile Gasketing</div>
    </div>
  </div>
  <p class="copy right" style="left:22px;top:480px;width:580px">Tile Gasketing products were created for our Nested Base Manufacturing customers. For those looking for the benefits of a proper gasketing solution, but jobs that are constantly changing, these tiles offer the best solution. By covering an entire MDF porous spoil board with these non-porous tiles, not only is the vacuum less likely to leak from tool paths that are being cut, but the sum of 1/4" holes creates a universal clamping system that holds entire sheets more effectively.</p>

  <div class="product-card" style="left:24px;top:562px">
    <div class="photo onboard" role="img" aria-label="Photo of wood boards held on on-board gasketing">
      <div class="label">On-Board<br>Gasketing</div>
    </div>
  </div>
  <p class="copy" style="left:185px;top:613px;width:560px">On-Board Gasketing is an adhesive-backed material that is placed directly on the surface of a fixture or spoil board. It creates excellent holding power when doing short-run jobs and a dedicated fixture is not desired. The vacuum that is centralized and concentrated to a part like this is not possible without</p>

  <div class="product-card" style="left:617px;top:669px">
    <div class="photo inboard" role="img" aria-label="Photo of in-board gasketing routed into a fixture board">
      <div class="label">In-Board<br>Gasketing</div>
    </div>
  </div>
  <p class="copy right" style="left:16px;top:720px;width:586px">In-Board Gasketing products are for creating dedicated fixtures for dedicated long-term parts. The benefits gained from utilizing a proper dedicated fixture are enormous. Placed in the pre-routed channels of a non-po-rous fixture board, these tools maximize vacuum performance, with accurate z-depth tolerances, extended tooling life, and more. If you are doing repetitive parts, do it with In-Board Gasketing.</p>

  <div class="product-card" style="left:24px;top:794px">
    <div class="photo cover" role="img" aria-label="Photo of rows of round cover gaskets">
      <div class="label">Cover<br>Gasketing</div>
    </div>
  </div>
  <p class="copy" style="left:172px;top:839px;width:580px">For making Dedicated Fixtures for the smallest of parts.&nbsp; Cover gasketing allows for maximum vacuum surface area based on the shape of your specific CAD part.</p>

  <footer class="footer">
    <div class="item" style="left:26px;top:19px">
      <svg width="16" height="16" viewBox="0 0 24 24"><path d="M6.6 10.8a15.1 15.1 0 0 0 6.6 6.6l2.2-2.2c.3-.3.7-.4 1-.2 1.1.4 2.3.6 3.6.6.6 0 1 .4 1 1V20c0 .6-.4 1-1 1A17 17 0 0 1 3 4c0-.6.4-1 1-1h3.5c.6 0 1 .4 1 1 0 1.3.2 2.5.6 3.6.1.3 0 .7-.2 1z"/></svg>
      <span style="font-size:15px">800-555-0142</span>
    </div>
    <div class="divider" style="left:186px"></div>
    <div class="item" style="left:227px;top:11px">
      <svg width="13" height="16" viewBox="0 0 24 30"><path d="M12 0a10 10 0 0 0-10 10c0 7.5 10 20 10 20s10-12.5 10-20A10 10 0 0 0 12 0zm0 14a4 4 0 1 1 0-8 4 4 0 0 1 0 8z"/></svg>
      <span>4820 Alder Creek Rd<br>Suite B Cedar Ridge, CA 95924</span>
    </div>
    <div class="divider" style="left:478px"></div>
    <div class="item" style="left:510px;top:10px;align-items:flex-start">
      <span style="display:flex;flex-direction:column;gap:6px;padding-top:2px">
        <svg width="13" height="13" viewBox="0 0 24 24"><path d="M12 2a10 10 0 1 0 0 20 10 10 0 0 0 0-20zm6.9 6h-3a15 15 0 0 0-1.3-3.9A8 8 0 0 1 18.9 8zM12 4c.8 1.2 1.5 2.5 1.9 4h-3.8c.4-1.5 1.1-2.8 1.9-4zM4.3 14a8 8 0 0 1 0-4h3.4a16 16 0 0 0 0 4zm.8 2h3a15 15 0 0 0 1.3 3.9A8 8 0 0 1 5.1 16zm3-8h-3a8 8 0 0 1 4.3-3.9C8.8 5.3 8.4 6.6 8.1 8zM12 20c-.8-1.2-1.5-2.5-1.9-4h3.8c-.4 1.5-1.1 2.8-1.9 4zm2.3-6H9.7a14 14 0 0 1 0-4h4.6a14 14 0 0 1 0 4zm.3 5.9c.6-1.2 1-2.5 1.3-3.9h3a8 8 0 0 1-4.3 3.9zm1.7-5.9a16 16 0 0 0 0-4h3.4a8 8 0 0 1 0 4z"/></svg>
        <svg width="13" height="11" viewBox="0 0 24 18"><path d="M0 0h24v18H0zm2 2v1l10 7 10-7V2zm0 3.5V16h20V5.5l-10 7z"/></svg>
      </span>
      <span>www.brixwellmfg.com<br>info@brixwellmfg.com</span>
    </div>
    <div class="social"><span></span><span></span></div>
  </footer>
  <div class="footer-base"></div>
</div>
</body>
</html>
```